Business Card Design

​Silver Harbor Grooves provides personal, friendly service in a fun and high energy environment. We are based in Vermont.

We would like a card that appeals to a wide range of audiences as we do a wide range of events. Please feel free to check out our website silverharborgrooves.com for inspiration.

Target Market(s)

weddings, corporate, birthday parties, colleges

Industry/Entity Type

Business

Contact Information for Business Card

Silver Harbor Grooves
Providing Entertainment For All Occasions
555 218 6093
silverharborgrooves@mailvane.com
silverharborgrooves.com

```html
<!DOCTYPE html>
<html lang="en">
<head>
<meta charset="utf-8">
<title>Silver Harbor Grooves — Business Card</title>
<link rel="stylesheet" href="https://fonts.googleapis.com/css2?family=Open+Sans:wght@400;600;700&display=swap">
<style>
  :root {
    --canvas: #ece9e4;
    --card-white: #ffffff;
    --brand-green: #2f6a1f;
    --brand-green-dark: #245316;
    --brand-maroon: #4a1414;
    --ink: #3a3a3a;
    --ink-soft: #6b6b6b;
    --back-black: #1a1514;
    --back-text: #f2f2f2;
  }
  * { box-sizing: border-box; margin: 0; padding: 0; }
  html, body { width: 1200px; height: 1200px; overflow: hidden; }
  body {
    background: var(--canvas);
    font-family: "Open Sans", Arial, sans-serif;
    display: flex;
    flex-direction: column;
    align-items: center;
    justify-content: center;
    gap: 60px;
  }
  .card {
    position: relative;
    width: 900px;
    height: 510px;
    border-radius: 34px;
    overflow: hidden;
    box-shadow: 0 6px 18px rgba(0,0,0,0.18);
  }

  /* Front */
  .card-front { background: var(--card-white); }
  .front-band { position: absolute; inset: 0; width: 100%; height: 100%; }
  .holder {
    position: absolute;
    top: 34px;
    right: 52px;
    text-align: right;
    color: #fff;
  }
  .holder-name { font-size: 30px; font-weight: 700; line-height: 1.2; }
  .holder-title { font-size: 22px; font-weight: 400; opacity: 0.9; }
  .brand-name {
    position: absolute;
    left: 70px;
    top: 250px;
    display: flex;
    align-items: center;
    gap: 16px;
    color: var(--brand-green);
    font-size: 38px;
    font-weight: 700;
    letter-spacing: 0.5px;
    text-transform: uppercase;
  }
  .brand-dot {
    width: 22px; height: 22px;
    border-radius: 50%;
    background: var(--brand-maroon);
  }
  .contact {
    position: absolute;
    left: 70px;
    bottom: 58px;
    display: flex;
    align-items: stretch;
    gap: 32px;
    color: var(--ink);
    font-size: 19px;
  }
  .contact-list { list-style: none; display: flex; flex-direction: column; gap: 8px; }
  .contact-list li { display: flex; align-items: center; gap: 10px; }
  .contact-icon { width: 18px; height: 18px; flex: none; }
  .contact-divider { width: 2px; background: #c9c9c9; }
  .contact-address { display: flex; flex-direction: column; gap: 8px; padding-top: 4px; color: var(--ink-soft); }

  /* Back */
  .card-back {
    background: var(--back-black);
    display: flex;
    flex-direction: column;
    align-items: center;
    justify-content: center;
    gap: 70px;
    color: var(--back-text);
  }
  .back-brand {
    display: flex;
    align-items: center;
    gap: 20px;
    font-size: 48px;
    font-weight: 700;
    text-transform: uppercase;
    letter-spacing: 1px;
  }
  .back-brand .brand-dot { width: 28px; height: 28px; background: var(--back-text); }
  .back-web { font-size: 28px; font-weight: 600; letter-spacing: 2px; }
</style>
</head>
<body>

  <section class="card card-front" aria-label="Business card front">
    <svg class="front-band" viewBox="0 0 900 510" preserveAspectRatio="none" aria-hidden="true">
      <path d="M0 0 H900 V250 C700 170 420 95 0 110 Z" fill="var(--brand-green)"/>
      <path d="M300 104 C520 110 720 175 900 250 V274 C720 205 520 130 300 104 Z" fill="var(--brand-maroon)"/>
    </svg>

    <div class="holder">
      <p class="holder-name">Your Name</p>
      <p class="holder-title">Title</p>
    </div>

    <div class="brand-name">
      <span class="brand-dot"></span>
      <span>Silver Harbor Grooves</span>
    </div>

    <div class="contact">
      <ul class="contact-list">
        <li>
          <svg class="contact-icon" viewBox="0 0 20 20" aria-hidden="true"><circle cx="10" cy="10" r="10" fill="var(--brand-green)"/><path d="M6.5 5.5l2 .2.8 2.3-1.2 1c.7 1.4 1.6 2.3 3 3l1-1.2 2.3.8.2 2c-4.6.6-8.7-3.5-8.1-8.1z" fill="#fff"/></svg>
          <span>555 218 6093</span>
        </li>
        <li>
          <svg class="contact-icon" viewBox="0 0 20 20" aria-hidden="true"><circle cx="10" cy="10" r="10" fill="var(--brand-green)"/><rect x="5" y="6.5" width="10" height="7" fill="#fff"/><path d="M5 6.5l5 4 5-4" stroke="var(--brand-green)" stroke-width="1.2" fill="none"/></svg>
          <span>silverharborgrooves@mailvane.com</span>
        </li>
        <li>
          <svg class="contact-icon" viewBox="0 0 20 20" aria-hidden="true"><circle cx="10" cy="10" r="10" fill="var(--brand-green)"/><circle cx="10" cy="10" r="5" stroke="#fff" stroke-width="1.3" fill="none"/><path d="M5 10h10M10 5c-2.5 3-2.5 7 0 10M10 5c2.5 3 2.5 7 0 10" stroke="#fff" stroke-width="1" fill="none"/></svg>
          <span>www.silverharborgrooves.com</span>
        </li>
      </ul>
      <span class="contact-divider"></span>
      <div class="contact-address">
        <span>Sreet Name, City Name</span>
        <span>Zip Code-00000</span>
      </div>
    </div>
  </section>

  <section class="card card-back" aria-label="Business card back">
    <div class="back-brand">
      <span class="brand-dot"></span>
      <span>Silver Harbor Grooves</span>
    </div>
    <p class="back-web">www.silverharborgrooves.com</p>
  </section>

</body>
</html>
```